Anzeigengestaltung für Steuerberater
Zielgruppe
aufgrund Unsimmitgkeiten mit pixelwerkhof.de, bitte ich Sie, diesen Event hier zu ignorieren.
Aufgabenstellung

```html
<!DOCTYPE html>
<html lang="de">
<head>
<meta charset="utf-8">
<title>Steuererklärung – halden</title>
<link href="https://fonts.googleapis.com/css2?family=Montserrat:wght@300;400;500;600;700;800&family=Roboto:wght@400;500&display=swap" rel="stylesheet">
<style>
:root{
  --navy:#0f2f7a;
  --royal:#0a3a9a;
  --orange:#e85d10;
  --orange-dark:#c2410c;
  --green:#8aa61a;
  --text:#555a66;
  --white:#ffffff;
  --popup-bg:#f6f7fb;
}
*{box-sizing:border-box;margin:0;padding:0}
html,body{width:813px;height:1200px;overflow:hidden}
body{position:relative;font-family:'Montserrat',sans-serif;background:var(--white);color:var(--text)}
.hero{position:absolute;left:0;top:0;width:813px;height:346px;
  background:linear-gradient(100deg,#7a3f18 0%,#5a4a3a 30%,#2e4a6a 60%,#1f3d66 85%,#2a4a40 100%)}
.site-header{position:absolute;left:0;top:0;width:813px;height:66px;border-bottom:1px solid rgba(255,255,255,.35)}
.brand{position:absolute;left:60px;top:10px;font-size:30px;font-weight:300;color:var(--white);letter-spacing:1px}
.nav{position:absolute;top:26px;left:299px;font-size:9px;font-weight:500;color:var(--white)}
.nav span{position:absolute;white-space:nowrap}
.nav .active{color:var(--orange)}
.nav-cta{position:absolute;left:665px;top:22px;width:89px;height:22px;border-radius:11px;background:var(--orange-dark);color:var(--white);font-size:6.5px;font-weight:600;display:flex;align-items:center;justify-content:center;gap:5px}
.hero-title{position:absolute;left:60px;top:131px;font-size:19px;font-weight:700;color:#e8e8e8;letter-spacing:.3px}
.hero-lead{position:absolute;left:60px;top:171px;font-size:10.5px;font-weight:300;color:var(--white);line-height:15px}
.hero-btn{position:absolute;left:60px;top:246px;width:123px;height:33px;border-radius:17px;background:var(--orange-dark);color:var(--white);font-size:7.5px;font-weight:600;display:flex;align-items:center;justify-content:center;gap:6px}
.content{position:absolute;left:65px;top:386px;width:688px;font-size:10.2px;font-weight:300;line-height:14px;color:#4a4f5a}
.content h1{font-size:20px;font-weight:700;color:var(--navy);margin-bottom:18px}
.content strong{color:var(--navy);font-weight:700}
.content p{margin-bottom:14px}
.content ul{list-style:none;margin-bottom:14px}
.content li::before{content:"•";color:#333;margin-right:5px}
.card{position:absolute;top:752px;width:169px;border-radius:14px;background:var(--white);box-shadow:0 2px 8px rgba(0,0,0,.12);overflow:hidden;text-align:center}
.card-tag{height:20px;background:var(--orange-dark);color:var(--white);font-size:9.5px;font-weight:700;line-height:20px}
.card-title{margin-top:12px;font-size:12.8px;font-weight:700;color:var(--navy);line-height:17px}
.card-title .price{color:#b85a14}
.features{list-style:none;text-align:left;margin:15px 2px 0 12px;font-size:7.9px;line-height:10.8px;color:#555}
.features li{position:relative;padding-left:13px;margin-bottom:7.8px}
.features li svg{position:absolute;left:0;top:1px}
.features .hl{color:var(--orange)}
.rule{height:1px;background:#ddd;margin:0 14px}
.note{font-size:6.8px;font-style:italic;font-weight:600;color:#333;text-align:left;margin:6px 14px 0}
.sub-note{font-size:6.5px;font-style:italic;color:#777;text-align:left;margin:5px 15px 0}
.sub-price{font-size:9.5px;color:var(--orange);margin-top:17px}
.cost-foot{text-align:justify;text-align-last:justify;font-size:9.5px;font-weight:700;color:#333;line-height:13px;margin:8px 0 0}
.cost-foot .last{text-align-last:left;display:block}
.calc-btn{display:flex;align-items:center;justify-content:center;gap:6px;height:32px;margin:16px 7px 0;border-radius:16px;background:var(--green);color:var(--white);font-size:7.5px;font-weight:600}
.badge{position:absolute;width:50px;height:50px;border-radius:50%;background:var(--green);border:2px solid #a9c23a;color:var(--white);text-align:center;font-weight:800;line-height:1}
.badge .ab{font-size:4px;display:block;margin-top:9px}
.badge .num{font-size:14px;display:block}
.badge .cur{font-size:7px;display:block}
.dim{position:absolute;inset:0;background:rgba(0,0,0,.5)}
.popup{position:absolute;left:222px;top:166px;width:369px;height:283px;border-radius:8px;background:var(--popup-bg);overflow:hidden;text-align:center}
.close{position:absolute;left:332px;top:10px;width:22px;height:22px;border-radius:50%;background:var(--white);border:1.5px solid #ccc;display:flex;align-items:center;justify-content:center}
.kicker{position:absolute;left:0;right:0;top:56px;font-size:13px;font-weight:700;color:var(--orange)}
.popup-title{position:absolute;left:0;right:0;top:74px;font-size:24px;font-weight:800;color:var(--royal)}
.popup-text{position:absolute;left:0;right:0;top:109px;font-family:'Roboto',sans-serif;font-size:16.5px;line-height:21px;color:#111}
.voucher{position:absolute;left:0;right:0;top:164px;font-family:'Roboto',sans-serif;font-size:13px;color:var(--orange)}
.popup-btn{position:absolute;left:110px;top:200px;width:149px;height:38px;border-radius:19px;background:var(--orange);color:var(--white);font-family:'Roboto',sans-serif;font-size:14.5px;display:flex;align-items:center;justify-content:center;gap:8px}
</style>
</head>
<body>

<div class="hero" role="img" aria-label="Hintergrundfoto: Luftaufnahme von Wald und Landschaft in warmen und blauen Tönen"></div>

<header class="site-header">
  <div class="brand">halden</div>
  <nav class="nav">
    <span style="left:0">Treuhandangebot ⌄</span>
    <span class="active" style="left:104px">Steuern</span>
    <span style="left:152px">Gründung ⌄</span>
    <span style="left:221px">Domizil</span>
    <span style="left:268px">News</span>
    <span style="left:306px">Über mich</span>
  </nav>
  <div class="nav-cta">KONTAKT/TERMIN <svg width="4" height="6" viewBox="0 0 4 6"><path d="M1 1l2 2-2 2" stroke="#fff" fill="none" stroke-width=".8"/></svg></div>
</header>

<h2 class="hero-title">STEUERERKLÄRUNG</h2>
<p class="hero-lead">Ihre Steuererklärung:<br>Endlich einfach.<br>Digital und Kompetent.</p>
<div class="hero-btn">ZU DEN PREISEN <svg width="5" height="8" viewBox="0 0 5 8"><path d="M1 1l3 3-3 3" stroke="#fff" fill="none" stroke-width="1"/></svg></div>

<main class="content">
  <h1>Steuerklärung aus einer Hand</h1>
  <p><strong>Warum ich mir Zeit für Sie nehme:</strong> Jede Steuererklärung ist einzigartig, und daher biete ich Ihnen eine individuelle Beratung – <strong>komplett digital und ohne persönlichen Termin.</strong></p>
  <p><strong>So funktioniert es:</strong></p>
  <p>Ich habe die Abläufe für Ihre Steuererklärung optimiert und digitalisiert, um es Ihnen so einfach wie möglich zu machen. Alle Dokumente und Informationen tauschen wir bequem über folgende Kanäle aus:</p>
  <ul>
    <li><strong>E-Mail:</strong> Für schnellen und unkomplizierten Austausch.</li>
    <li><strong>Telefon oder Videocall:</strong> Für individuelle Beratungsgespräche.</li>
    <li><strong>Postweg:</strong> Für den Fall, dass Sie Ihre Unterlagen lieber in Papierform einreichen möchten.</li>
  </ul>
  <p><strong>Ihre Vorteile:</strong></p>
  <ul>
    <li>Keine Anfahrtswege oder Terminvereinbarungen vor Ort.</li>
    <li>Schnelle und effiziente Bearbeitung dank digitaler Prozesse.</li>
    <li>Maximale Flexibilität – Sie entscheiden, wie wir kommunizieren.</li>
  </ul>
  <p><strong>Meine Leistungen für Ihre Steuererklärung biete ich zu den folgenden Konditionen an:</strong></p>
</main>

<svg width="0" height="0" style="position:absolute"><defs><symbol id="tick" viewBox="0 0 9 8"><path d="M1 4.2l2.4 2.6L8 1" stroke="#e85d10" stroke-width="1.5" fill="none"/></symbol></defs></svg>

<section class="card" style="left:65px;padding-bottom:14px">
  <div class="card-tag">STEUERERKLÄRUNG</div>
  <h3 class="card-title">EINZELPERSONEN OHNE<br>LIEGENSCHAFT<br><span class="price">AB CHF 180.-</span></h3>
  <ul class="features">
    <li><svg width="8" height="7"><use href="#tick"/></svg>Telefonische Beratung 15 Minuten</li>
    <li><svg width="8" height="7"><use href="#tick"/></svg>wenige Positionen im Wertschrif­ten- und Schuldenverzeichnis</li>
    <li><svg width="8" height="7"><use href="#tick"/></svg>Erstellen der Steuererklärung</li>
    <li><svg width="8" height="7"><use href="#tick"/></svg>Maximierung der Steuerabzüge</li>
  </ul>
  <div class="rule" style="margin-top:12px"></div>
  <p class="sub-note">Einzelpersonen mit Liegenschaft</p>
  <p class="sub-price">AB CHF 280.-</p>
  <ul class="features" style="margin-top:16px">
    <li><svg width="8" height="7"><use href="#tick"/></svg>Telefonische Beratung 15 Minuten</li>
    <li><svg width="8" height="7"><use href="#tick"/></svg>wenige Positionen im Wertschrif­ten- und Schuldenverzeichnis</li>
    <li><svg width="8" height="7"><use href="#tick"/></svg>ohne effektiven Liegenschaftsunterhalt</li>
    <li><svg width="8" height="7"><use href="#tick"/></svg>Erstellen der Steuererklärung</li>
    <li><svg width="8" height="7"><use href="#tick"/></svg>Maximierung der Steuerabzüge</li>
  </ul>
  <p class="cost-foot">zzgl. aufwandsspezifischer <span class="last">Kosten</span></p>
</section>

<section class="card" style="left:280px;padding-bottom:9px">
  <div class="card-tag">STEUERERKLÄRUNG</div>
  <h3 class="card-title">PREMIUM-PAKET<br>ONLINE<br><span class="price">AB CHF 245.-</span></h3>
  <ul class="features">
    <li><svg width="8" height="7"><use href="#tick"/></svg>Telefonische Beratung</li>
    <li><svg width="8" height="7"><use href="#tick"/></svg>Kontrolle erhaltener Dokumente</li>
    <li><svg width="8" height="7"><use href="#tick"/></svg>Erstellen der Steuererklärung</li>
    <li><svg width="8" height="7"><use href="#tick"/></svg>Beantragen der Fristverlängerung</li>
    <li><svg width="8" height="7"><use href="#tick"/></svg>Maximierung der Steuerabzüge</li>
    <li class="hl"><svg width="8" height="7"><use href="#tick"/></svg>Kontrolle und telefonische Bespre­chung der Veranlagung</li>
    <li class="hl"><svg width="8" height="7"><use href="#tick"/></svg>Kontrolle der Steuerrechnungen</li>
  </ul>
  <div class="rule" style="margin-top:10px"></div>
  <p class="note">zzgl. aufwandsspezifischer Kosten</p>
  <div class="calc-btn">JETZT PREIS BERECHNEN <svg width="4" height="7" viewBox="0 0 4 7"><path d="M1 1l2 2.5-2 2.5" stroke="#fff" fill="none" stroke-width=".8"/></svg></div>
</section>

<section class="card" style="left:496px;padding-bottom:9px">
  <div class="card-tag">STEUERERKLÄRUNG</div>
  <h3 class="card-title">PREMIUM-PAKET<br>PERSÖNLICH<br><span class="price">AB CHF 445.-</span></h3>
  <ul class="features">
    <li><svg width="8" height="7"><use href="#tick"/></svg>Telefonische Beratung</li>
    <li><svg width="8" height="7"><use href="#tick"/></svg>Kontrolle erhaltener Dokumente</li>
    <li><svg width="8" height="7"><use href="#tick"/></svg>Erstellen der Steuererklärung</li>
    <li><svg width="8" height="7"><use href="#tick"/></svg>Beantragen der Fristverlängerung</li>
    <li><svg width="8" height="7"><use href="#tick"/></svg>Maximierung der Steuerabzüge</li>
    <li class="hl"><svg width="8" height="7"><use href="#tick"/></svg>Kontrolle und telefonische Bespre­chung der Veranlagung</li>
    <li class="hl"><svg width="8" height="7"><use href="#tick"/></svg>Kontrolle der Steuerrechnungen</li>
    <li class="hl"><svg width="8" height="7"><use href="#tick"/></svg>Vertretung gegenüber Steuerbehörden</li>
    <li class="hl"><svg width="8" height="7"><use href="#tick"/></svg>Persönliche Beratung</li>
  </ul>
  <div class="rule" style="margin-top:10px"></div>
  <p class="note">zzgl. aufwandsspezifischer Kosten</p>
  <div class="calc-btn">JETZT PREIS BERECHNEN <svg width="4" height="7" viewBox="0 0 4 7"><path d="M1 1l2 2.5-2 2.5" stroke="#fff" fill="none" stroke-width=".8"/></svg></div>
</section>

<div class="badge" style="left:414px;top:817px"><span class="ab">AB</span><span class="num">245</span><span class="cur">CHF</span></div>
<div class="badge" style="left:629px;top:823px"><span class="ab">AB</span><span class="num">445</span><span class="cur">CHF</span></div>

<div class="dim"></div>

<aside class="popup">
  <div class="close"><svg width="9" height="9" viewBox="0 0 9 9"><path d="M1 1l7 7M8 1L1 8" stroke="#555" stroke-width="1.2"/></svg></div>
  <p class="kicker">VITAMIN C FÜR</p>
  <h2 class="popup-title">IHRE STEUERERKLÄRUNG</h2>
  <p class="popup-text">Einfach und erfrischend!<br>Profitieren Sie jetzt von Ihrem 30.</p>
  <p class="voucher">Neukunden-Gutschein</p>
  <div class="popup-btn">Jetzt Anfordern <svg width="6" height="10" viewBox="0 0 6 10"><path d="M1 1l4 4-4 4" stroke="#fff" fill="none" stroke-width="1.3"/></svg></div>
</aside>

</body>
</html>
```